BUSINESS CARD, LETTERHEAD ENVELOPES FOR VIDEO PRODUCTION COMPANY
NO SUBTITLE NECESSARY - PLEASE UPLOAD WINNING LOGO FOR ME!!!
Simple
Owen Marsh
Founder
Corporate Offices: 700 Central Expressway  Suite 550 Fairview, TX 75094​
866.41.BLOOM (866.412.5666)
owen@lumaharbor.com
www.lumaharbor.com
Looking for a very clean, simple design that shows off the logo...GOOD LUCK!!!
OUR SERVICES & AREAS OF EXPERTISE Corporate Trainings & Events Individual Spotlights Client Testimonials Music Venues & City Festivals Legal & Court Depositions Non-Profit Fundraisers

```html
<!DOCTYPE html>
<html lang="en">
<head>
<meta charset="utf-8">
<title>Luma Harbor Stationery</title>
<link rel="stylesheet" href="https://fonts.googleapis.com/css2?family=Lato:wght@400;700&display=swap">
<style>
  :root {
    --bg: #cfd0d2;
    --paper: #ffffff;
    --paper-shade: #f1f2f3;
    --teal: #1aa69b;
    --dark: #333536;
    --ink: #4a4c4e;
    --muted: #8a8c8e;
  }
  * { box-sizing: border-box; margin: 0; padding: 0; }
  html, body { width: 1200px; height: 1000px; overflow: hidden; }
  body {
    background: var(--bg);
    font-family: "Lato", sans-serif;
    color: var(--ink);
    position: relative;
  }
  .piece { position: absolute; background: var(--paper); box-shadow: 0 4px 14px rgba(0,0,0,.18); overflow: hidden; }

  .brand { display: flex; align-items: center; gap: 8px; color: var(--teal); font-weight: 400; white-space: nowrap; }
  .brand .mark { background: var(--teal); flex: none; }

  .contact { font-size: 8px; line-height: 1.5; color: var(--ink); }

  /* Letterhead */
  .letterhead { left: 270px; top: 120px; width: 300px; height: 420px; }
  .letterhead .brand { position: absolute; left: 26px; top: 30px; font-size: 17px; }
  .letterhead .brand .mark { width: 24px; height: 24px; }
  .letterhead .contact-top { position: absolute; right: 22px; top: 28px; text-align: right; }
  .letterhead .address { position: absolute; right: 22px; bottom: 50px; text-align: right; }
  .letterhead .footer { position: absolute; left: 0; bottom: 0; width: 100%; height: 34px; }

  /* Second sheet */
  .sheet { left: 650px; top: 100px; width: 310px; height: 440px; }
  .sheet .brand { position: absolute; left: 50%; top: 50%; transform: translate(-50%,-50%); font-size: 19px; }
  .sheet .brand .mark { width: 30px; height: 30px; }

  /* Business cards */
  .card { left: 110px; width: 184px; height: 104px; }
  .card-front { top: 620px; }
  .card-front .brand { position: absolute; left: 12px; top: 16px; font-size: 10px; gap: 5px; }
  .card-front .brand .mark { width: 14px; height: 14px; }
  .card-front .person { position: absolute; right: 12px; top: 15px; text-align: right; }
  .person .name { font-size: 9px; font-weight: 700; color: var(--dark); }
  .person .role { font-size: 7px; color: var(--muted); }
  .card-front .band { position: absolute; left: 0; top: 50px; width: 100%; height: 12px; }
  .card-front .contact { position: absolute; left: 12px; top: 68px; font-size: 6px; line-height: 1.45; }

  .card-back { top: 750px; background: var(--dark); }
  .card-back .brand { position: absolute; left: 12px; top: 18px; font-size: 10px; gap: 5px; }
  .card-back .brand .mark { width: 14px; height: 14px; }
  .card-back .band { position: absolute; left: 0; top: 44px; width: 100%; height: 12px; }
  .card-back .contact { position: absolute; left: 12px; top: 64px; font-size: 6px; line-height: 1.45; color: #d6d7d8; }

  /* Envelopes */
  .envelope-front { left: 340px; top: 690px; width: 350px; height: 175px; background: var(--paper-shade); }
  .envelope-front .brand { position: absolute; left: 50%; top: 48px; transform: translateX(-50%); font-size: 17px; }
  .envelope-front .brand .mark { width: 26px; height: 26px; }
  .envelope-front .contact { position: absolute; left: 24px; top: 100px; font-size: 7px; }

  .envelope-back { left: 740px; top: 690px; width: 350px; height: 175px; background: var(--paper-shade); }
  .envelope-back svg { position: absolute; inset: 0; }
</style>
</head>
<body>

  <section class="piece letterhead">
    <div class="brand"><span class="mark"></span>Luma Harbor</div>
    <div class="contact contact-top">
      866.41.BLOOM<br>866.412.5666<br>owen@lumaharbor.com<br>www.lumaharbor.com
    </div>
    <div class="contact address">418 Harlow Parkway Suite 220<br>Fairview, TX 75094</div>
    <svg class="footer" viewBox="0 0 300 34" preserveAspectRatio="none">
      <rect x="0" y="6" width="300" height="28" fill="#333536"/>
      <polygon points="205,6 300,6 300,34 222,34" fill="#1aa69b"/>
      <polygon points="196,0 300,0 300,6 205,6" fill="#1aa69b"/>
    </svg>
  </section>

  <section class="piece sheet">
    <div class="brand"><span class="mark"></span>Luma Harbor</div>
  </section>

  <section class="piece card card-front">
    <div class="brand"><span class="mark"></span>Luma Harbor</div>
    <div class="person">
      <div class="name">Owen Marsh</div>
      <div class="role">Founder</div>
    </div>
    <svg class="band" viewBox="0 0 184 12" preserveAspectRatio="none">
      <rect x="0" y="0" width="120" height="12" fill="#333536"/>
      <polygon points="120,0 184,0 184,12 112,12" fill="#1aa69b"/>
    </svg>
    <div class="contact">866.412.5666<br>owen@lumaharbor.com<br>www.lumaharbor.com</div>
  </section>

  <section class="piece card card-back">
    <div class="brand"><span class="mark"></span>Luma Harbor</div>
    <svg class="band" viewBox="0 0 184 12" preserveAspectRatio="none">
      <polygon points="70,0 184,0 184,12 62,12" fill="#1aa69b"/>
    </svg>
    <div class="contact">418 Harlow Parkway Suite 220<br>Fairview, TX 75094<br>www.lumaharbor.com</div>
  </section>

  <section class="piece envelope-front">
    <div class="brand"><span class="mark"></span>Luma Harbor</div>
    <div class="contact">866.41.BLOOM<br>866.412.5666<br>owen@lumaharbor.com<br>www.lumaharbor.com</div>
  </section>

  <section class="piece envelope-back">
    <svg viewBox="0 0 350 175" preserveAspectRatio="none">
      <polyline points="0,175 175,70 350,175" fill="none" stroke="#d9dadb" stroke-width="1"/>
      <polygon points="0,0 350,0 175,70" fill="#1aa69b"/>
      <circle cx="175" cy="58" r="22" fill="#1aa69b"/>
    </svg>
  </section>

</body>
</html>
```